Travel, Resort and Tourism Advisor

I am looking for a classy and slick website for a travel, resort and tourism website which will offer first hand advise to tourist and fun seekers on the best locations and remarkable places to relax and unwind. We are primary located in the United States but will offer services to people worldwide. My website will feature images and locations and analysis of the best resorts in the Industry. Designers can take an idea from http://wanderquill.example It will include prices, safety tips, culture and how to make the best of your tourism. The website will compare different destinations and recommend places based on the user budget, culture, and ethnic nationality. I would want a colorful and attention seeking website. Have questions ask.

```html
<!DOCTYPE html>
<html lang="en">
<head>
<meta charset="utf-8">
<title>Marlow Advisors – Travel, Resort and Tourism</title>
<link rel="stylesheet" href="https://fonts.googleapis.com/css2?family=Open+Sans:wght@400;600;700&family=Roboto+Condensed:wght@400;700&display=swap">
<style>
:root{
  --green:#2f9a3f;
  --green-dark:#277f34;
  --green-bright:#1fdc2a;
  --ink:#333;
  --muted:#666;
  --line:#ddd;
  --star:#f2a22c;
  --panel:#f2f2f2;
  --footer:#eeeeee;
  --bottom:#2b2b2b;
  --white:#fff;
}
*{box-sizing:border-box;margin:0;padding:0}
html,body{width:1200px;height:2466px;overflow:hidden}
body{position:relative;background:var(--white);font-family:"Open Sans",Arial,sans-serif;color:var(--ink);font-size:12px}
.abs{position:absolute}
.cond{font-family:"Roboto Condensed","Arial Narrow",sans-serif}

/* header */
.site-header{left:0;top:0;width:1200px;height:88px}
.brand{left:98px;top:26px;font-family:"Roboto Condensed",sans-serif;font-weight:700;font-size:30px;color:var(--green);display:flex;align-items:center;gap:8px}
.brand-dot{width:22px;height:22px;border-radius:50%;background:var(--green)}
.top-nav{left:656px;top:36px;font-size:12px;color:#444}
.top-nav span{margin:0 5px;color:#999}
.lang{left:994px;top:28px;width:106px;height:32px;border:1px solid var(--line);font-size:10px;color:#666;display:flex;align-items:center;padding-left:12px;gap:6px}
.lang i{display:block;width:14px;height:10px;background:#c33;border:1px solid #ccc}

/* search band */
.search-band{left:0;top:88px;width:1200px;height:78px;background:var(--green)}
.search-input{top:16px;height:44px;background:var(--white);font-size:11px;color:#666;display:flex;align-items:center;padding:0 16px;justify-content:space-between}
.search-btn{left:840px;top:16px;width:146px;height:44px;background:#333;color:#fff;font-size:15px;display:flex;align-items:center;justify-content:center}

/* hero */
.hero{left:0;top:166px;width:1200px;height:472px;background:linear-gradient(180deg,#3f5a4a 0%,#2f5048 40%,#2d6f72 70%,#1f4f55 100%)}
.hero h1{position:absolute;left:0;width:1200px;top:128px;text-align:center;font-family:"Roboto Condensed",sans-serif;font-size:50px;color:#fff;font-weight:700}
.hero .sub{position:absolute;left:0;width:1200px;top:190px;text-align:center;font-family:"Roboto Condensed",sans-serif;font-size:22px;color:#fff;font-weight:700}
.booking{left:213px;top:234px;width:777px;height:100px;background:rgba(255,255,255,.35);border:2px solid rgba(255,255,255,.7);border-radius:4px}
.radios{position:absolute;left:20px;top:10px;display:flex;gap:26px;color:#fff;font-size:15px}
.radios label{display:flex;align-items:center;gap:6px}
.radios i{width:13px;height:13px;border-radius:50%;background:#fff;border:1px solid #aaa;display:block}
.radios i.on{box-shadow:inset 0 0 0 3px #fff;background:#333}
.field{position:absolute;top:42px;height:40px;background:#fff;font-size:11px;color:#666;display:flex;align-items:center;justify-content:space-between;padding:0 14px}
.go{position:absolute;left:650px;top:42px;width:112px;height:40px;background:var(--green);color:#fff;font-size:14px;font-weight:600;display:flex;align-items:center;justify-content:center}
.dots{left:556px;top:362px;display:flex;gap:10px;align-items:center}
.dots i{display:block;width:12px;height:12px;border-radius:50%;background:#fff}
.dots i.ring{width:22px;height:22px;background:none;border:2px solid #fff;position:relative}
.dots i.ring::after{content:"";position:absolute;left:4px;top:4px;width:10px;height:10px;border-radius:50%;background:#fff}

/* section titles */
.section-title{font-family:"Roboto Condensed",sans-serif;font-size:24px;color:#333;border-bottom:2px solid var(--line);padding-bottom:10px}
.section-title::after{content:"";position:absolute;left:0;bottom:-2px;width:60px;height:2px;background:var(--green)}

/* place cards */
.place{width:218px}
.place .photo{width:218px;height:158px}
.place .row{display:flex;justify-content:space-between;margin-top:12px;font-size:14px;color:#444}
.stars{color:var(--star);font-size:11px;letter-spacing:1px}
.stars b{color:#ccc;font-weight:400}
.place p{margin-top:8px;font-size:11px;line-height:17px;color:#555}

/* travel tips */
.tip{width:206px;height:110px;border-bottom:1px solid #eee}
.tip .avatar{position:absolute;left:4px;top:0;width:60px;height:60px;border-radius:50%}
.tip .date{position:absolute;left:14px;top:68px;color:var(--green);font-size:11px}
.tip h4{position:absolute;left:78px;top:0;font-family:"Roboto Condensed",sans-serif;font-weight:400;font-size:15px;line-height:20px;color:#333}
.tip p{position:absolute;left:78px;top:44px;font-size:10.5px;line-height:16px;color:#555}

/* testimonial */
.testimonial{left:98px;top:1585px;width:698px;height:141px;border:1px solid var(--line)}
.testimonial .avatar{position:absolute;left:20px;top:20px;width:96px;height:96px;border-radius:50%}
.testimonial q{position:absolute;left:140px;top:20px;width:540px;font-style:italic;font-size:11.5px;line-height:23px;color:#666;quotes:none}
.testimonial .who{position:absolute;left:142px;top:98px;font-size:12px;color:#666}
.testimonial .who b{color:#1f3b7a}

/* sidebar */
.newsletter{left:833px;top:735px;width:267px;height:223px;background:var(--panel)}
.newsletter h5{position:absolute;left:66px;top:26px;font-size:12px;font-weight:600;line-height:19px;color:#333}
.newsletter .env{position:absolute;left:14px;top:24px}
.newsletter p{position:absolute;left:14px;top:80px;font-size:10.5px;line-height:18px;color:#555}
.newsletter .email{position:absolute;left:14px;top:126px;width:238px;height:36px;border:1px solid var(--line);background:#fff;font-size:10px;color:#666;padding:11px}
.newsletter .sub-btn{position:absolute;left:14px;top:174px;width:106px;height:32px;background:var(--green);color:#fff;font-size:11px;display:flex;align-items:center;justify-content:center}
.newsletter .sq{position:absolute;top:180px;width:20px;height:20px}

.review{left:833px;width:267px;height:128px;border-bottom:1px solid #e6e6e6}
.review .avatar{position:absolute;left:2px;top:0;width:80px;height:80px;border-radius:50%;border:3px solid #eee}
.review h6{position:absolute;left:100px;top:0;font-weight:400;font-size:13px;color:#555}
.review .meta{position:absolute;left:100px;top:22px;font-size:12px;color:#444}
.review p{position:absolute;left:100px;top:44px;font-size:10.5px;line-height:18px;color:#555}

.video-card{left:833px;top:1437px;width:267px;height:288px;background:linear-gradient(180deg,#3d86c6 0%,#7bb4dd 45%,#9fcf9a 70%,#3f5f3a 100%)}
.video-card .play{position:absolute;left:108px;top:104px;width:50px;height:50px;border-radius:50%;border:2px solid rgba(255,255,255,.8);background:rgba(0,0,0,.25)}
.video-card .tag{position:absolute;left:16px;top:200px;background:#e6b316;color:#222;font-size:10px;font-weight:700;padding:2px 8px}
.video-card h5{position:absolute;left:16px;top:224px;color:#fff;font-weight:400;font-size:16px}
.video-card p{position:absolute;left:16px;top:250px;color:#fff;font-size:14px}

/* social */
.social-band{left:0;top:1784px;width:1200px;height:62px;background:var(--green-bright)}
.social{position:absolute;top:17px;display:flex;align-items:center;gap:10px;color:#fff;font-family:"Roboto Condensed",sans-serif;font-weight:700;font-size:14px}
.social i{display:block;width:30px;height:30px;border-radius:50%;background:#fff;opacity:.9}
.strip{left:0;top:1846px;width:1200px;height:188px;display:flex}
.strip div{flex:1;height:188px}
.follow{left:530px;top:1932px;width:150px;height:36px;background:rgba(40,40,40,.8);color:#fff;font-size:12px;display:flex;align-items:center;justify-content:center}

.countries{left:108px;top:2052px;font-size:12px;color:#333;display:flex;gap:15px}
.countries b{color:var(--green);font-weight:600}

/* footer */
.footer{left:0;top:2083px;width:1200px;height:268px;background:var(--footer)}
.fcol{position:absolute;top:36px}
.fcol h5{font-family:"Roboto Condensed",sans-serif;font-weight:400;font-size:16px;color:#333;margin-bottom:12px}
.fcol li{list-style:none;font-size:11px;line-height:22.5px;color:#444}
.fcol li::before{content:"»";margin-right:9px;color:#777}
.contact h5{color:#1f3b7a}
.contact .org{font-size:11px;color:#444;line-height:20px}
.contact .line{display:flex;align-items:center;gap:14px;font-size:12px;color:#444;margin-top:10px}
.badge{position:absolute;top:2267px;width:98px;height:34px;background:#111;border-radius:5px}

.bottom{left:0;top:2351px;width:1200px;height:115px;background:var(--bottom)}
.bottom .copy{position:absolute;left:0;width:1200px;top:34px;text-align:center;color:#fff;font-size:10px}
.bottom .icons{position:absolute;left:523px;top:64px;display:flex;gap:8px}
.bottom .icons i{display:block;width:26px;height:26px;border:1px solid #aaa;border-radius:50%}
</style>
</head>
<body>

<header class="abs site-header">
  <div class="abs brand"><span>Marlow Advisors</span><span class="brand-dot"></span></div>
  <nav class="abs top-nav">Home<span>/</span>Login<span>/</span>Register<span>/</span>Post a Job (Free!)<span>/</span>Blog</nav>
  <div class="abs lang"><i></i>ENGLISH <span style="margin-left:12px">⌄</span></div>
</header>

<section class="abs search-band">
  <div class="abs search-input" style="left:213px;width:292px">I'm Looking for..
    <svg width="14" height="14" viewBox="0 0 14 14"><circle cx="6" cy="6" r="4.5" fill="none" stroke="#333" stroke-width="1.8"/><line x1="9.3" y1="9.3" x2="13" y2="13" stroke="#333" stroke-width="1.8"/></svg></div>
  <div class="abs search-input" style="left:505px;width:335px;background:#f3f3f3;border-left:1px solid #ddd">Enter a Destinations
    <svg width="10" height="14" viewBox="0 0 10 14"><path d="M5 0a5 5 0 0 1 5 5c0 4-5 9-5 9S0 9 0 5a5 5 0 0 1 5-5z" fill="#333"/><circle cx="5" cy="5" r="1.8" fill="#f3f3f3"/></svg></div>
  <div class="abs search-btn">SEARCH</div>
</section>

<section class="abs hero" role="img" aria-label="Tropical lagoon resort with palm trees and a thatched bungalow">
  <h1>BOOK ACTIVITIES</h1>
  <div class="sub">YOUR ADVENTURE STARTS HERE</div>
  <div class="abs booking">
    <div class="radios">
      <label><i class="on"></i>Hotels</label><label><i></i>Flights</label><label><i></i>Holiday</label>
      <label><i></i>Rentals</label><label><i></i>Restaurants</label><label><i></i>Destinations</label>
    </div>
    <div class="field" style="left:16px;width:298px">City or hotel name <span>▾</span></div>
    <div class="field" style="left:324px;width:154px">dd/mm/yy <span>▦</span></div>
    <div class="field" style="left:488px;width:152px">dd/mm/yy <span>▦</span></div>
    <div class="go">LET'S GO!</div>
  </div>
  <div class="abs dots"><i class="ring"></i><i></i><i></i><i></i></div>
</section>

<h2 class="abs section-title" style="left:98px;top:672px;width:698px">Most Popular Places</h2>

<article class="abs place" style="left:98px;top:735px"><div class="photo" role="img" aria-label="Paris tower at sunset" style="background:linear-gradient(180deg,#6aa6d8,#e6c55a 60%,#5c7a2a)"></div><div class="row">Italian Dream Tour<span class="stars">★★★<b>☆☆</b></span></div><p>Nemo enim ipsam voluptatem quia voptas sit aspernatur aut</p></article>
<article class="abs place" style="left:337px;top:735px"><div class="photo" role="img" aria-label="Kayakers paddling on turquoise water" style="background:linear-gradient(180deg,#2fb0c4,#45c9d3 50%,#2a8fa8)"></div><div class="row">Italian Dream Tour<span class="stars">★★★<b>☆☆</b></span></div><p>Nemo enim ipsam voluptatem quia voptas sit aspernatur aut</p></article>
<article class="abs place" style="left:577px;top:735px"><div class="photo" role="img" aria-label="Longtail boat on a tropical beach with limestone cliffs" style="background:linear-gradient(180deg,#3a8ad0,#8ec8e6 45%,#4aa7b8 70%,#e8dcc0)"></div><div class="row">Italian Dream Tour<span class="stars">★★★<b>☆☆</b></span></div><p>Nemo enim ipsam voluptatem quia voptas sit aspernatur aut</p></article>
<article class="abs place" style="left:98px;top:991px"><div class="photo" role="img" aria-label="Backpacker standing on a coastal cliff" style="background:linear-gradient(180deg,#5fa9d9,#9fd0e8 55%,#c9b27a)"></div><div class="row">Italian Dream Tour<span class="stars">★★★<b>☆☆</b></span></div><p>Nemo enim ipsam voluptatem quia voptas sit aspernatur aut</p></article>
<article class="abs place" style="left:337px;top:991px"><div class="photo" role="img" aria-label="Beach hut among palm trees" style="background:linear-gradient(180deg,#3b8fd6,#7cc2e3 45%,#3c8a3a 70%,#cbb98e)"></div><div class="row">Italian Dream Tour<span class="stars">★★★<b>☆☆</b></span></div><p>Nemo enim ipsam voluptatem quia voptas sit aspernatur aut</p></article>
<article class="abs place" style="left:577px;top:991px"><div class="photo" role="img" aria-label="Family playing in the snow" style="background:linear-gradient(180deg,#d8e4ec,#b3c9d8 50%,#c9493a 80%,#e8eef2)"></div><div class="row">Italian Dream Tour<span class="stars">★★★<b>☆☆</b></span></div><p>Nemo enim ipsam voluptatem quia voptas sit aspernatur aut</p></article>

<h2 class="abs section-title" style="left:98px;top:1256px;width:698px">Travel Tips</h2>

<article class="abs tip" style="left:98px;top:1325px"><div class="avatar" role="img" aria-label="Traveller portrait" style="background:#7aa85a"></div><span class="date">July 07</span><h4>Tips to Avoid Over<br>Packing for Your Trip</h4><p>Sed ut perspiciatis dmnis<br>iste natus error sit</p></article>
<article class="abs tip" style="left:343px;top:1325px"><div class="avatar" role="img" aria-label="Traveller portrait" style="background:#c9a58a"></div><span class="date">July 07</span><h4>Tips to Avoid Over<br>Packing for Your Trip</h4><p>Sed ut perspiciatis dmnis<br>iste natus error sit</p></article>
<article class="abs tip" style="left:590px;top:1325px"><div class="avatar" role="img" aria-label="Group of travellers" style="background:#6aa0c9"></div><span class="date">July 07</span><h4>Tips to Avoid Over<br>Packing for Your Trip</h4><p>Sed ut perspiciatis dmnis<br>iste natus error sit</p></article>
<article class="abs tip" style="left:98px;top:1453px"><div class="avatar" role="img" aria-label="Traveller portrait" style="background:#8a7a60"></div><span class="date">July 07</span><h4>Tips to Avoid Over<br>Packing for Your Trip</h4><p>Sed ut perspiciatis dmnis<br>iste natus error sit</p></article>
<article class="abs tip" style="left:343px;top:1453px"><div class="avatar" role="img" aria-label="Traveller portrait" style="background:#3a3f4a"></div><span class="date">July 07</span><h4>Tips to Avoid Over<br>Packing for Your Trip</h4><p>Sed ut perspiciatis dmnis<br>iste natus error sit</p></article>
<article class="abs tip" style="left:590px;top:1453px"><div class="avatar" role="img" aria-label="Traveller portrait" style="background:#c99a6a"></div><span class="date">July 07</span><h4>Tips to Avoid Over<br>Packing for Your Trip</h4><p>Sed ut perspiciatis dmnis<br>iste natus error sit</p></article>

<blockquote class="abs testimonial">
  <div class="avatar" role="img" aria-label="Portrait of the manager" style="background:#d8d8d8"></div>
  <q>“ Lorem ipsum dolor sit amet, consectetur adipiscing elit, sed do eiusmod tempor incididunt ut labore et dolore magna aliqua. Ut enim ad minim veniam, quis nostrud exercitation ullamco laboris nisi ut aliquip ex ea commodo consequat. Duis aute irure dolor in reprehenderit ”</q>
  <div class="who"><b>John Doe</b> - Manager &nbsp; ‹ ›</div>
</blockquote>

<h2 class="abs section-title" style="left:833px;top:668px;width:267px">Tips For Your Next Holiday</h2>
<aside class="abs newsletter">
  <svg class="env" width="40" height="40" viewBox="0 0 40 40"><rect x="2" y="10" width="36" height="26" fill="var(--green)"/><path d="M2 10l18 14 18-14" fill="none" stroke="#fff" stroke-width="2"/><rect x="10" y="2" width="20" height="14" fill="#fff" stroke="var(--green)" stroke-width="2"/></svg>
  <h5>SUBSCRIBE TO OUR FREE WEEKLY<br>TRAVELNOTE NEWSLETTER!</h5>
  <p>Get the latest deals, reviews &amp; articles.<br>Tailored for the destinations you choose.</p>
  <div class="email">Email Address</div>
  <div class="sub-btn">SUBSCRIBE</div>
  <span class="sq" style="left:128px;background:#3b5998"></span>
  <span class="sq" style="left:152px;background:#1da1f2"></span>
</aside>

<h2 class="abs section-title" style="left:833px;top:978px;width:267px">Hotel Reviews</h2>
<article class="abs review" style="top:1052px"><div class="avatar" role="img" aria-label="Couple portrait" style="background:#d9c2a8"></div><h6>Nemo enim ipsam volup</h6><div class="meta"><span class="stars">★★★<b>☆☆</b></span> &nbsp; 188 Reviews</div><p>Sed ut perspiciatis unde omnis<br>iste natus error sit</p></article>
<article class="abs review" style="top:1180px"><div class="avatar" role="img" aria-label="Couple portrait" style="background:#b8a08a"></div><h6>Nemo enim ipsam volup</h6><div class="meta"><span class="stars">★★★<b>☆☆</b></span> &nbsp; 188 Reviews</div><p>Sed ut perspiciatis unde omnis<br>iste natus error sit</p></article>
<article class="abs review" style="top:1309px"><div class="avatar" role="img" aria-label="Couple portrait" style="background:#7c8fa8"></div><h6>Nemo enim ipsam volup</h6><div class="meta"><span class="stars">★★★<b>☆☆</b></span> &nbsp; 188 Reviews</div><p>Sed ut perspiciatis unde omnis<br>iste natus error sit</p></article>

<article class="abs video-card" role="img" aria-label="Family walking on a tropical beach">
  <span class="play"></span>
  <span class="tag">TRAVEL</span>
  <h5>VACATIONS</h5>
  <p>Family, friends, couples or ..</p>
</article>

<section class="abs social-band">
  <div class="social" style="left:215px"><i></i>PALBOOK</div>
  <div class="social" style="left:362px"><i></i>CHIRPER</div>
  <div class="social" style="left:505px"><i></i>SNAPGRAM</div>
  <div class="social" style="left:659px"><i></i>ORBIT PLUS</div>
  <div class="social" style="left:826px"><i></i>VIEWTUBE</div>
</section>

<section class="abs strip">
  <div role="img" aria-label="Sunset over the sea with birds" style="background:linear-gradient(180deg,#3b2a20,#e08a2a 55%,#2a1a10)"></div>
  <div role="img" aria-label="Beach with lounging traveller" style="background:linear-gradient(180deg,#5aa8d8,#9fd6e4 50%,#e6dcc4)"></div>
  <div role="img" aria-label="Tent at dusk" style="background:linear-gradient(180deg,#7a2a2a,#c04a3a 50%,#3a2a2a)"></div>
  <div role="img" aria-label="Island lagoon" style="background:linear-gradient(180deg,#4a8a5a,#3fb8c8 60%,#1f7a8a)"></div>
  <div role="img" aria-label="Couple with a map in a city" style="background:linear-gradient(180deg,#e8d6b8,#c8a67a 60%,#8a6a4a)"></div>
  <div role="img" aria-label="Hiker at sunrise" style="background:linear-gradient(180deg,#f4d27a,#e89a2a 55%,#6a4a2a)"></div>
  <div role="img" aria-label="Couple on a beach under a palm" style="background:linear-gradient(180deg,#2f7ad0,#7ec0e6 50%,#f0e6d0)"></div>
</section>
<div class="abs follow">FOLLOW SNAPGRAM</div>

<nav class="abs countries"><b>Other Countries / Regions :</b><span>United States</span><span>England</span><span>Scotland</span><span>Wales</span><span>Ireland</span><span>Spain</span><span>Belgium</span><span>Denmark</span><span>Germany</span><span>Italy</span><span>Poland</span><span>South Africa</span><span>India</span></nav>

<footer class="abs footer">
  <div class="fcol" style="left:98px"><h5>BEST HILL STATIONS</h5><ul><li>Vacationing in France</li><li>Napa Valley</li><li>Los Angeles</li><li>Vacationing in Scandinavian Europe</li><li>The Whitmore Astra</li><li>Belvoir Saint Clair Hotel</li></ul></div>
  <div class="fcol" style="left:372px"><h5>POPULAR PILGRIMAGES</h5><ul><li>Vacationing in France</li><li>Napa Valley</li><li>Los Angeles</li><li>Vacationing in Scandinavian Europe</li><li>The Whitmore Astra</li><li>Belvoir Saint Clair Hotel</li></ul></div>
  <div class="fcol" style="left:611px"><h5>BEST &nbsp;BEACHES</h5><ul><li>Vacationing in France</li><li>Napa Valley</li><li>Los Angeles</li><li>Vacationing in Scandinavian Europe</li><li>The Whitmore Astra</li><li>Belvoir Saint Clair Hotel</li></ul></div>
  <div class="fcol contact" style="left:871px"><h5>CONTACT US</h5>
    <div class="org">MARLOW ADVISORS<br>18 Fernhill Lane, Ashbrook</div>
    <div class="line"><svg width="16" height="16" viewBox="0 0 16 16"><path d="M3 1l3 3-2 2c1 2 3 4 5 5l2-2 3 3-2 3C7 15 1 9 1 3z" fill="none" stroke="#444" stroke-width="1.3"/></svg>+1 555 0142 7788</div>
    <div class="line" style="margin-top:6px"><svg width="16" height="12" viewBox="0 0 16 12"><rect x="1" y="1" width="14" height="10" fill="none" stroke="#444" stroke-width="1.3"/><path d="M1 1l7 6 7-6" fill="none" stroke="#444" stroke-width="1.3"/></svg>info@marlowadvisors.example</div>
  </div>
</footer>
<span class="badge" style="left:880px"></span>
<span class="badge" style="left:998px"></span>

<section class="abs bottom">
  <div class="copy">©2014 - 2016 MARLOW ADVISORS .. ALL RIGHTS RESERVED.</div>
  <div class="icons"><i></i><i></i><i></i><i></i><i></i></div>
</section>

</body>
</html>
```